Simple elegant business card

General card for a fin and television director.
Just want name, email, phone and address.

Target Market(s)

Prospective employers

Industry/Entity Type

Business

Requirements
Must have
• As above
Nice to have
• Logo but not necessary.
Should not have
• Not too colourful or funky.
• Simplicity and elegance the way to go.

```html
<!DOCTYPE html>
<html lang="en">
<head>
<meta charset="utf-8">
<title>Nora Vance – Business Card</title>
<link href="https://fonts.googleapis.com/css2?family=Mr+De+Haviland&family=Quicksand:wght@400;500&display=swap" rel="stylesheet">
<style>
  :root {
    --page-bg: #3a3a3c;
    --card-black: #060606;
    --card-grey: #2a2a2c;
    --silver-light: #f2f2f2;
    --silver-mid: #b9b9bb;
    --silver-dark: #6d6d70;
    --text-silver: #d8d8da;
  }
  * { margin: 0; padding: 0; box-sizing: border-box; }
  html, body {
    width: 1200px;
    height: 1000px;
    overflow: hidden;
    background: var(--page-bg);
  }
  .business-card {
    position: absolute;
    left: 150px;
    top: 243px;
    width: 900px;
    height: 514px;
    overflow: hidden;
    background:
      linear-gradient(150deg, var(--card-black) 0%, var(--card-black) 38%, var(--card-grey) 62%, #141415 100%);
    box-shadow: 0 18px 40px rgba(0, 0, 0, 0.45);
  }
  .card-name {
    position: absolute;
    left: 20px;
    top: 20px;
    padding: 50px 90px 50px 90px;
    font-family: "Mr De Haviland", cursive;
    font-weight: 400;
    font-size: 180px;
    line-height: 1;
    color: var(--silver-light);
    background: linear-gradient(180deg, #ffffff 0%, var(--silver-mid) 55%, #ffffff 100%);
    -webkit-background-clip: text;
    background-clip: text;
    -webkit-text-fill-color: transparent;
    filter: drop-shadow(0 2px 1px rgba(0, 0, 0, 0.8));
    white-space: nowrap;
  }
  .card-role {
    position: absolute;
    left: 60px;
    top: 350px;
    font-family: "Quicksand", sans-serif;
    font-weight: 500;
    font-size: 22px;
    letter-spacing: 2px;
    color: var(--text-silver);
  }
  .card-contact {
    position: absolute;
    left: 455px;
    top: 336px;
    font-family: "Quicksand", sans-serif;
    font-size: 26px;
    letter-spacing: 2px;
    color: var(--text-silver);
    list-style: none;
  }
  .card-contact li {
    display: flex;
    align-items: center;
    height: 38px;
  }
  .contact-icon {
    width: 22px;
    height: 22px;
    margin-right: 20px;
    fill: none;
    stroke: var(--silver-mid);
    stroke-width: 1.6;
  }
  .silver-band {
    position: absolute;
    left: 0;
    bottom: 0;
    width: 100%;
    height: 62px;
    background: linear-gradient(180deg, var(--silver-dark) 0%, var(--silver-light) 30%, var(--silver-mid) 70%, var(--silver-dark) 100%);
  }
</style>
</head>
<body>
  <article class="business-card">
    <h1 class="card-name">Nora Vance</h1>
    <p class="card-role">TV/FILM DIRECTOR</p>
    <ul class="card-contact">
      <li>
        <svg class="contact-icon" viewBox="0 0 24 24" aria-hidden="true">
          <path d="M7 3h3l1 5-2 1.5a11 11 0 0 0 5.5 5.5L16 13l5 1v3a3 3 0 0 1-3 3A15 15 0 0 1 4 6a3 3 0 0 1 3-3z"/>
        </svg>
        <span>+1 310 555 0142</span>
      </li>
      <li>
        <svg class="contact-icon" viewBox="0 0 24 24" aria-hidden="true">
          <rect x="2" y="5" width="20" height="14"/>
          <path d="M2 5l10 8 10-8"/>
        </svg>
        <span>noravance@mail.com</span>
      </li>
    </ul>
    <div class="silver-band"></div>
  </article>
</body>
</html>
```